my website is tabellepiece.com. (brand name is ta belle pièce) This is just a template that i have choose for. The content and the pictures are not about my business just the template.
I would like to have 4 pages for now. 1 homepage, which will be an overview for all pages, it is right now in this way. It will directly highlight my story. My website will tell an exclusive story about details which makes the difference and will make people happy with very small things. It will be art related but very stylish as well. I also want to have a event agenda on my homepage where people can see where my next event is. Page 2 my blog, where I will write weekly about mindset, lifestyle and details. Inspiration place for people who are looking for unique and exclusive approaches in life. Page 3 shop, where I will sell my stuff which is handmade and unique, it will be limited edition stuff. Mostly I will make the designs from marbling art, which I am a teacher for. (https://www.vidorastream.com/watch?v=Kq7TbWm2Xa) check this video out for more. Page 4 is book page. Here people will be able to book private or group classes for marbling art (check the video). I have already a community of more than 500 people on join ring, which will be my public as well. I wanna implement the join ring button on this page as well. to be able to track.

This is about my website. I also need a logo for my brand, which will suit my website and my goals.

I can also give you a reference website, which really like as structure and style;
https://www.brightmorrowco.com/products/the-daybook-organizer?ref=Xp4RtLm8QzVw2NbKc7HsJd9FgTy3MvEqBa6WnUoZr1LkPxYhGiCe5DsAtQfVbNj0HmRwKyXo8LcTpZaEsUv2GqDnIwMb

ta belle pièce

4 page

• I can also give you a reference website, which really like as structure and style;
• https://www.brightmorrowco.com/products/the-daybook-organizer?ref=Xp4RtLm8QzVw2NbKc7HsJd9FgTy3MvEqBa6WnUoZr1LkPxYhGiCe5DsAtQfVbNj0HmRwKyXo8LcTpZaEsUv2GqDnIwMb

```html
<!DOCTYPE html>
<html lang="en">
<head>
<meta charset="utf-8">
<title>ta belle pièce — Home</title>
<link rel="stylesheet" href="https://fonts.googleapis.com/css2?family=Montserrat:wght@400;500&family=Pacifico&family=Playfair+Display:wght@400;700&display=swap">
<style>
:root{
  --ink:#111111;
  --text:#555555;
  --muted:#888888;
  --rule:#d6d6d6;
  --white:#ffffff;
  --panel:#3f3c3c;
  --footer:#2f2f2f;
  --footer-bar:#1b1b1b;
  --accent:#e0245e;
  --btn:#000000;
}
*{box-sizing:border-box;margin:0;padding:0}
html,body{width:1200px;height:2995px;overflow:hidden;background:var(--white)}
body{position:relative;font-family:"Playfair Display",Georgia,serif;color:var(--text)}
.abs{position:absolute}
.sans{font-family:"Montserrat",Arial,sans-serif}
.script{font-family:"Pacifico",cursive}

/* header */
.site-header{position:absolute;left:0;top:0;width:1200px;height:82px;background:var(--white)}
.nav-link{position:absolute;top:32px;font:400 14px "Montserrat",Arial,sans-serif;color:var(--ink);letter-spacing:.5px}
.nav-link.active{border-bottom:1px solid var(--ink);padding-bottom:6px}
.brand{position:absolute;left:458px;top:20px;display:flex;align-items:center;gap:12px}
.brand-dot{width:40px;height:40px;border-radius:50%;background:var(--accent)}
.brand-name{font:400 30px "Playfair Display",Georgia,serif;color:var(--ink)}
.header-icons{position:absolute;left:1118px;top:28px;display:flex;gap:12px}

/* hero */
.hero{position:absolute;left:0;top:82px;width:1200px;height:504px;
  background:radial-gradient(ellipse at 50% 45%,#2a2a2a 0%,#141414 55%,#6f6a63 100%)}
.hero-kicker{position:absolute;left:0;width:1200px;top:160px;text-align:center;font:400 25px "Pacifico",cursive;color:var(--white)}
.hero-title{position:absolute;left:0;width:1200px;top:212px;text-align:center;font:400 44px "Playfair Display",Georgia,serif;color:var(--white)}
.btn-outline{position:absolute;border:1px solid var(--white);color:var(--white);font:400 13px "Montserrat",Arial,sans-serif;display:flex;align-items:center;justify-content:center;letter-spacing:.5px}

/* product */
.product-image{position:absolute;left:92px;top:700px;width:414px;height:400px;
  background:linear-gradient(135deg,#d98bd8 0%,#c56bc4 40%,#e38a5a 60%,#d77fd2 100%)}
.product-title{position:absolute;left:610px;top:684px;font:400 50px "Pacifico",cursive;color:var(--ink)}
.rule{position:absolute;height:1px;background:var(--rule)}
.price{position:absolute;left:612px;top:790px;font:700 16px "Playfair Display",Georgia,serif;color:var(--ink)}
.btn-solid{position:absolute;background:var(--btn);color:var(--white);font:700 13px "Playfair Display",Georgia,serif;display:flex;align-items:center;justify-content:center;letter-spacing:.5px}
.body-copy{position:absolute;font-size:12.5px;line-height:22px;color:var(--muted)}

/* story */
.section-title{position:absolute;left:92px;font:400 36px "Playfair Display",Georgia,serif;color:var(--ink)}

/* event */
.event-panel{position:absolute;left:92px;top:1402px;width:498px;height:454px;background:var(--panel)}
.event-vertical{position:absolute;left:-52px;top:200px;width:220px;transform:rotate(-90deg);font:400 34px "Pacifico",cursive;color:#5a5656;white-space:nowrap}
.event-title{position:absolute;left:114px;top:30px;font:400 34px "Playfair Display",Georgia,serif;color:var(--white)}
.event-sub{position:absolute;left:114px;top:86px;font:400 34px "Pacifico",cursive;color:var(--white)}
.event-date{position:absolute;left:114px;top:162px;font:700 11px "Playfair Display",Georgia,serif;color:var(--white)}
.event-copy{position:absolute;left:114px;top:194px;width:340px;font:700 12px/20px "Playfair Display",Georgia,serif;color:#e8e8e8}
.event-image{position:absolute;left:590px;top:1402px;width:518px;height:454px;
  background:linear-gradient(170deg,#b8403a 0%,#6b5a48 22%,#9fcfd8 40%,#a9d4c8 70%,#8aa56a 100%)}
.dot{position:absolute;top:1900px;width:10px;height:10px;border-radius:50%;border:1px solid #bbb}
.dot.on{border:2px solid var(--ink)}

/* blog */
.blog-card{position:absolute;top:2124px;width:328px}
.blog-image{width:328px;height:274px}
.blog-title{margin-top:44px;font:700 18px "Playfair Display",Georgia,serif;color:var(--ink)}
.blog-meta{margin-top:2px;font-size:10px;color:var(--text)}
.blog-copy{margin-top:16px;font-size:12px;line-height:18px;color:var(--text)}

/* footer */
.site-footer{position:absolute;left:0;top:2734px;width:1200px;height:224px;background:var(--footer)}
.footer-bar{position:absolute;left:0;top:2958px;width:1200px;height:37px;background:var(--footer-bar)}
.footer-heading{position:absolute;top:62px;font:400 17px "Playfair Display",Georgia,serif;color:var(--white)}
.footer-list{position:absolute;top:94px;list-style:none;font:400 12px/21px "Playfair Display",Georgia,serif;color:#dddddd}
.footer-list li::before{content:"» ";}
.email-field{position:absolute;left:784px;top:90px;width:222px;height:32px;border:1px solid #555;background:#2a2a2a;color:#ccc;font-size:12px;padding:8px 12px}
.social{position:absolute;top:11px;width:16px;height:16px;border-radius:50%;border:1px solid #ccc}
</style>
</head>
<body>

<header class="site-header">
  <span class="nav-link active" style="left:196px">HOME</span>
  <span class="nav-link" style="left:318px">MY BLOG</span>
  <div class="brand"><span class="brand-dot"></span><span class="brand-name">ta belle pièce</span></div>
  <span class="nav-link" style="left:818px">SHOP</span>
  <span class="nav-link" style="left:940px">BOOK ME</span>
  <div class="header-icons">
    <svg width="16" height="16" viewBox="0 0 16 16" fill="none" stroke="#111" stroke-width="1.4"><circle cx="8" cy="5" r="3.2"/><path d="M2 15c0-3.5 2.7-5.5 6-5.5s6 2 6 5.5"/></svg>
    <svg width="18" height="16" viewBox="0 0 18 16" fill="none" stroke="#111" stroke-width="1.4"><path d="M1 1h3l2 9h9l2-7H5"/><circle cx="7" cy="14" r="1.3"/><circle cx="14" cy="14" r="1.3"/></svg>
  </div>
</header>

<section class="hero" role="img" aria-label="Photo of a marbling tray filled with dark water and floating colour">
  <p class="hero-kicker">Different tools can be used for the creation of Ebru art.</p>
  <h1 class="hero-title">Do you want to know about that</h1>
  <a class="btn-outline" style="left:542px;top:290px;width:136px;height:36px">BOOK ME</a>
</section>

<section class="product">
  <div class="product-image" role="img" aria-label="Pink and orange marbled glitter artwork"></div>
  <h2 class="product-title">Glitter Art</h2>
  <div class="rule" style="left:612px;top:774px;width:496px"></div>
  <p class="price">$2495 USD</p>
  <a class="btn-solid" style="left:612px;top:832px;width:126px;height:34px">ADD TO CART</a>
  <p class="body-copy" style="left:612px;top:888px;width:490px">The paint was painted on the jelly and then scraped off with paper. Today, special Ebru paints are used. No jelly is needed anymore. The modern Ebru paints help to break the surface of the water. The Ebru paints are not mixable with water. The Ebru paint can not mix with water or the other colors, because different Ebru paints have a consistency and the different size of molecules. The Ebru colors can be painted into ornamental patterns with different techniques. Natural marble patterns are possible.</p>
</section>

<div class="rule" style="left:92px;top:1176px;width:1016px"></div>

<section class="story">
  <h2 class="section-title" style="top:1224px">My story</h2>
  <p class="body-copy" style="left:300px;top:1232px;width:810px;font-size:12px;line-height:20px;color:var(--text)">Welcome All! This Page will highlight the details about everything. Ta belle pièce - The details are not the details. They make the design! Lorem ipsum dolor sit amet, consectetur adipiscing elit. Nunc a tellus tellus. Donec malesuada magna at quam bibendum iaculis. Donec faucibus, justo id semper pretium, quam purus luctus erat, id lobortis lorem orci vitae quam. Etiam consectetur pellentesque elit sit amet lacinia. Donec eget vulputate elit. Donec et lectus eget magna lacinia porttitor vitae at nibh. Nullam quis eleifend purus. Nulla eu dui sit amet nibh dignissim finibus.</p>
</section>

<section class="event">
  <div class="event-panel">
    <span class="event-vertical">Upcoming event</span>
    <h3 class="event-title">Art Theraphy</h3>
    <p class="event-sub">Marbling workshop</p>
    <p class="event-date">October 16 - 1:30 PM</p>
    <p class="event-copy">The Turkish Art Of Marbling Are your interested in Art? Did you ever try the Turkish Marbling Art? Which has a great history from the thirteenth century. Dancing colors on water, will relax your mind.. Ebru Art is A Great mediation by making your Art! ~Marbling is the art of creating colorful patterns by sprinkling and brushing color pigments on a pan of oily water and then transforming this pattern to paper~</p>
    <a class="btn-outline" style="left:116px;top:366px;width:118px;height:36px;font-family:'Playfair Display',Georgia,serif;font-weight:700">KNOW MORE</a>
  </div>
  <div class="event-image" role="img" aria-label="Photo of a marbling tray with floral patterns and paint bottles"></div>
  <span class="dot on" style="left:578px"></span>
  <span class="dot" style="left:595px"></span>
  <span class="dot" style="left:610px"></span>
</section>

<div class="rule" style="left:92px;top:1962px;width:1016px"></div>

<section class="blog">
  <h2 class="section-title" style="top:2004px">My blog</h2>
  <p class="body-copy" style="left:266px;top:2012px;width:800px;font-size:12px;color:var(--text)">It is  about mindset, lifestyle and details. Inspiration place for people who are looking for unique and exclusive approaches in life.</p>

  <article class="blog-card" style="left:92px">
    <div class="blog-image" role="img" aria-label="Photo of a brown marbling tray with white veins" style="background:linear-gradient(160deg,#6d5e58 0%,#8a4a3e 45%,#9a5446 100%)"></div>
    <h3 class="blog-title">Paints with oil can be used</h3>
    <p class="blog-meta">02 October 2017 | Admin</p>
    <p class="blog-copy">The marbling of objects is also very popular. Special paints are used for creating Ebru art on plastic and metals. These patterns are created by the flotation of colors on the surface of water or very soft jelly. ....read more</p>
  </article>
  <article class="blog-card" style="left:436px">
    <div class="blog-image" role="img" aria-label="Photo of purple and white marbled pattern on water" style="background:linear-gradient(160deg,#6f6a72 0%,#7a3a5a 50%,#c9b7c4 100%)"></div>
    <h3 class="blog-title">Paints with oil can be used</h3>
    <p class="blog-meta">02 October 2017 | Admin</p>
    <p class="blog-copy">The marbling of objects is also very popular. Special paints are used for creating Ebru art on plastic and metals. These patterns are created by the flotation of colors on the surface of water or very soft jelly. ....read more</p>
  </article>
  <article class="blog-card" style="left:780px">
    <div class="blog-image" role="img" aria-label="Photo of a hand drawing a pink marbled pattern" style="background:linear-gradient(160deg,#b07a78 0%,#a4606a 50%,#c79a98 100%)"></div>
    <h3 class="blog-title">Paints with oil can be used</h3>
    <p class="blog-meta">02 October 2017 | Admin</p>
    <p class="blog-copy">The marbling of objects is also very popular. Special paints are used for creating Ebru art on plastic and metals. These patterns are created by the flotation of colors on the surface of water or very soft jelly. ....read more</p>
  </article>

  <a class="btn-solid" style="left:506px;top:2636px;width:140px;height:38px">MORE STORIES</a>
</section>

<footer class="site-footer">
  <div class="abs" style="left:92px;top:70px;display:flex;align-items:center;gap:10px">
    <span style="width:48px;height:48px;border-radius:50%;background:#7a7a7a;display:block"></span>
  </div>
  <p class="abs" style="left:190px;top:78px;width:216px;font:700 11px/17px 'Playfair Display',Georgia,serif;color:var(--white)">Welcome All! This Page will highlight the details about everything. Ta belle pièce - The details are not the details. They make the design!</p>

  <h4 class="footer-heading" style="left:436px">Quick Links</h4>
  <ul class="footer-list" style="left:436px"><li>Home</li><li>Blog</li><li>Shop</li><li>Book Me</li></ul>

  <h4 class="footer-heading" style="left:620px">Help</h4>
  <ul class="footer-list" style="left:620px"><li>Store Policy</li><li>Shipping &amp; Delivery</li><li>Customer Support</li><li>Order Status</li></ul>

  <h4 class="footer-heading" style="left:788px">Email Subscription</h4>
  <div class="email-field">Email</div>
  <a class="btn-solid" style="left:1016px;top:90px;width:92px;height:32px;font-size:11px">SUBMIT</a>
</footer>

<div class="footer-bar">
  <p class="abs" style="left:92px;top:12px;font:700 11px 'Playfair Display',Georgia,serif;color:var(--white)">Copyright © 2017 ta belle pièce</p>
  <span class="social" style="left:1034px"></span>
  <span class="social" style="left:1056px"></span>
  <span class="social" style="left:1078px"></span>
</div>

</body>
</html>
```